Letterhead Design Project

Please see attached logo as well as information below which could be relevant to design. Let me know if you have any questions.

Derek J. Holloman
Estate Planning and Insurance Specialist
Dholloman@brenwickfinancial.com
P: 516-471-2958 F: 516-471-3085
www.brenwickfinancial.com
4300 Maple Ridge Road, Suite 305E
Syosset, New York 11804

```html
<!DOCTYPE html>
<html lang="en">
<head>
<meta charset="UTF-8">
<title>Brenwick Financial Group – Letterhead</title>
<link href="https://fonts.googleapis.com/css2?family=Montserrat:wght@400;500;600;700&display=swap" rel="stylesheet">
<style>
  :root {
    --ink-navy: #23252f;
    --gold: #cdb585;
    --gold-deep: #b99d66;
    --paper: #ffffff;
    --text-dark: #1f1f1f;
    --text-light: #ffffff;
  }
  html, body {
    margin: 0;
    padding: 0;
    width: 900px;
    height: 1200px;
    overflow: hidden;
    background: var(--paper);
  }
  .letterhead {
    position: relative;
    width: 900px;
    height: 1200px;
    background: var(--paper);
    font-family: "Montserrat", Arial, sans-serif;
    overflow: hidden;
  }
  .header-shapes, .footer-shapes {
    position: absolute;
    left: 0;
    width: 900px;
  }
  .header-shapes { top: 0; height: 240px; }
  .footer-shapes { bottom: 0; height: 240px; }
  .header-shapes .band-dark, .footer-shapes .band-dark { fill: var(--ink-navy); }
  .header-shapes .band-gold, .footer-shapes .band-gold { fill: var(--gold); }

  .brand {
    position: absolute;
    top: 22px;
    left: 26px;
    display: flex;
    align-items: center;
    gap: 14px;
  }
  .brand-square {
    width: 58px;
    height: 58px;
    background: var(--gold);
  }
  .brand-name {
    color: var(--text-light);
    font-weight: 500;
    font-size: 30px;
    letter-spacing: 2px;
    text-transform: uppercase;
    white-space: nowrap;
  }

  .sender {
    position: absolute;
    top: 238px;
    left: 30px;
  }
  .sender-name {
    margin: 0;
    color: var(--gold-deep);
    font-weight: 500;
    font-size: 36px;
    line-height: 1.1;
  }
  .sender-title {
    margin: 6px 0 0;
    color: var(--text-dark);
    font-weight: 700;
    font-size: 14px;
  }

  .contact {
    position: absolute;
    left: 285px;
    top: 1078px;
    color: var(--text-light);
    font-size: 15px;
    line-height: 30px;
  }
  .contact-row { display: flex; gap: 40px; white-space: nowrap; }
  .contact-row .label { color: var(--gold); font-weight: 600; margin-right: 6px; }
  .contact-row .phone-item { width: 170px; }
  .contact-row .web-item { width: 250px; }
</style>
</head>
<body>
<div class="letterhead">
  <svg class="header-shapes" viewBox="0 0 900 240" aria-hidden="true">
    <path class="band-gold" d="M260,160 Q620,60 900,70 V235 Q700,110 260,160 Z"/>
    <path class="band-dark" d="M0,0 H900 V80 Q520,50 0,150 Z"/>
  </svg>

  <div class="brand">
    <div class="brand-square"></div>
    <div class="brand-name">Brenwick Financial Group</div>
  </div>

  <div class="sender">
    <h1 class="sender-name">Derek J. Holloman</h1>
    <p class="sender-title">Estate Planning and Insurance Specialist</p>
  </div>

  <svg class="footer-shapes" viewBox="0 960 900 240" aria-hidden="true">
    <path class="band-gold" d="M0,1200 V1040 Q450,960 900,1055 V1200 Z"/>
    <path class="band-dark" d="M0,1200 V1112 Q430,1010 900,1072 V1200 Z"/>
  </svg>

  <div class="contact">
    <div class="contact-row">
      <span class="phone-item"><span class="label">T:</span>516-471-2958</span>
      <span><span class="label">F:</span>516-471-3085</span>
    </div>
    <div class="contact-row">
      <span class="web-item"><span class="label">W:</span>www.brenwickfinancial.com</span>
      <span><span class="label">E:</span>Dholloman@brenwickfinancial.com</span>
    </div>
    <div class="contact-row">
      <span><span class="label">A:</span>4300 Maple Ridge Road, Suite 305E Syosset, New York 11804</span>
    </div>
  </div>
</div>
</body>
</html>
```